Existing Logo Post Card Design for Residential and Commercial Services Company

We are looking for a Post card design for bulk mail along with letterhead and business cards for a new Residential and Commercial Services company. We focus on senior citizens and vets with the idea of "One Call Every Service". We provide landscaping, pressure washing, maid service, and pest control to both the commercial and residential market. We also provide estimates, proposal creation, scheduling, cost controls and consulting to contractors.
The mailer is going to be targeting the residential services portion of the business and heading out to advertise our landscaping, pressure washing and maid services. It should use the primary color of red, white and blue. If the logo need to be tweaked on shades, please feel free to do that. More than just service we sell security to our customers because we are not the average residential services company.
The sample business card designs that have been uploaded are from another company that we currently own and we like the cards. We would like to keep it simple on the back of the card with the colors and the company slogan of “One Call Every Service”.
We also like the layout of the front of the card with the logo boldly displayed. The company name should also be display on the card “Taldrim Works” Please make sure there is a name, address, phone number, email address and website www.taldrimworks.example on the front of the card as well.
We would like the letter head to display the logo in the top left of the page with space for phone number, address, and website at the bottom of the page. We would like the info at the bottom of the page to be in a straight line across the bottom of the page. The page dimensions should be 8.5X11” and there should be a .5” margin around the complete perimeter of the page.
Thanks and good luck

Target Market(s)

Homeowners with a focus on Senior citizens and Vets

Industry/Entity Type

Residential Construction

Contact Information for Business Card

The business card should focus on Red, white and blue it will be 2 sided and should be bold and will be foiled.

Font styles to use
Serif

Requirements
Must have
• The Company slogan should be displayed on the back side of the card "One Call Every Service" it should also be easy to read
Nice to have
• The card should be Red, White, Blue and primarily black text.
Should not have
• Please refrain hard to read text it should be clear and easy to read

```html
<!DOCTYPE html>
<html lang="en">
<head>
<meta charset="utf-8">
<title>Taldrim Works – Letterhead Options</title>
<link rel="stylesheet" href="https://fonts.googleapis.com/css2?family=Oswald:wght@600;700&family=Source+Sans+3:wght@400&family=Montserrat:ital,wght@1,500&display=swap">
<style>
  :root {
    --canvas: #ffffff;
    --paper: #e6e6e8;
    --brand-red: #ed2227;
    --brand-navy: #2b3a67;
    --ink: #2d2d2d;
    --rule: #1a1a1a;
    --footer-dark: #231f20;
    --footer-text: #ffffff;
    --ghost: #e9d6d4;
  }
  * { margin: 0; padding: 0; box-sizing: border-box; }
  html, body {
    width: 1200px; height: 462px; overflow: hidden;
    background: var(--canvas);
  }
  .board { position: relative; width: 1200px; height: 462px; }

  .option-label {
    position: absolute; top: 243px;
    font-family: "Source Sans 3", sans-serif;
    font-size: 38px; font-weight: 400; color: #000;
  }
  .option-label--one { left: 28px; }
  .option-label--two { left: 1008px; }

  .letterhead {
    position: absolute; top: 0; width: 375px; height: 462px;
    background: var(--paper); overflow: hidden;
  }
  .letterhead--one { left: 222px; }
  .letterhead--two { left: 620px; }

  .letterhead__swoosh { position: absolute; top: 0; left: 0; }
  .swoosh-fill { fill: var(--brand-red); }
  .swoosh-edge { fill: none; stroke: var(--rule); stroke-width: 1.4; }

  .wordmark {
    position: absolute; top: 58px;
    font-family: "Oswald", sans-serif; font-weight: 700;
    color: var(--brand-navy);
    font-size: 21px; line-height: 19px; letter-spacing: 0.5px;
    text-transform: uppercase;
  }
  .letterhead--one .wordmark { right: 27px; text-align: right; }
  .letterhead--two .wordmark { left: 27px; }

  .ghost-name {
    position: absolute; top: 182px; left: 26px; width: 325px;
    font-family: "Oswald", sans-serif; font-weight: 700;
    font-size: 86px; line-height: 1; letter-spacing: 2px;
    color: var(--ghost); text-align: center; text-transform: uppercase;
  }

  .footer {
    position: absolute; left: 0; bottom: 0; width: 375px; height: 24px;
    display: flex; align-items: center; justify-content: center;
    font-family: "Montserrat", sans-serif; font-style: italic; font-weight: 500;
    font-size: 5.4px; color: var(--footer-text); white-space: nowrap;
  }
  .footer--red { background: var(--brand-red); border-top: 2px solid var(--rule); }
  .footer--dark { background: var(--footer-dark); border-top: 2px solid var(--brand-red); }
  .footer__sep { margin: 0 4px; }
</style>
</head>
<body>
<main class="board">

  <div class="option-label option-label--one">Option 01</div>

  <section class="letterhead letterhead--one">
    <svg class="letterhead__swoosh" width="375" height="62" viewBox="0 0 375 62">
      <path class="swoosh-fill" d="M0 0 H375 V3 C340 30 310 55 268 55 C200 55 110 35 0 0 Z"/>
      <path class="swoosh-edge" d="M0 0 C110 35 200 55 268 55 C310 55 340 30 375 3"/>
    </svg>
    <div class="wordmark">Taldrim<br>Works</div>
    <footer class="footer footer--red">
      1280 Harbor Crest Rd. Alvena, Texas, United States<span class="footer__sep">|</span>(555) 014-2290<span class="footer__sep">|</span>www.taldrimworks.example
    </footer>
  </section>

  <section class="letterhead letterhead--two">
    <svg class="letterhead__swoosh" width="375" height="62" viewBox="0 0 375 62">
      <path class="swoosh-fill" d="M0 0 H375 V3 C265 35 175 55 115 55 C70 55 35 30 0 3 Z"/>
      <path class="swoosh-edge" d="M0 3 C35 30 70 55 115 55 C175 55 265 35 375 3"/>
    </svg>
    <div class="wordmark">Taldrim<br>Works</div>
    <div class="ghost-name" aria-hidden="true">Taldrim</div>
    <footer class="footer footer--dark">
      1280 Harbor Crest Rd. Alvena, Texas, United States<span class="footer__sep">|</span>(555) 014-2290<span class="footer__sep">|</span>www.taldrimworks.example
    </footer>
  </section>

  <div class="option-label option-label--two">Option 02</div>

</main>
</body>
</html>
```